High-end Management Consulting Website

I am looking for a design that feels very high end and professional and very serious feeling. I would like a site that uses a lot of white space, with colors in the blue, grey family. You can use a very small about of the orange and green in the logo, but it needs to be a very small amount.

I like images similar to a rock climber helping another one up a mountain. I would love other imagery throughout the site of mountain ranges and people making it to the top.

When you think of the feel imagine people in suites, very corporate feeling. Very much focused on helping company leadership and CEOs solve problems.

From a functionality standpoint https://ninebramwell.com has a good deal of similar content- However, I do not like the colors or the design. I like graphics on websites similar to https://www.harrowcapitalgroup.com.

I like clean with lots of white space.

The link below has all of the content and design comments. https://files.quillnet.com/doc/7QpLm3XzR8vTt2KwYh5NbD9sFgJc4EuA6oViWr0Ue/view?share=open

Target Market(s)

High end businesses and very experienced executives.

Industry/Entity Type

Consulting

Coding

Coded - Design and coding required

Number of Pages Required

5+ page

Font styles to use
Sans Serif

Colors

Designer to choose colors to be used in the design.

Requirements
Must have
• white space, blues some gray, clean feel VERY LITTLE use of accent colors.

I want to have a centered navigation bar.
I would like to have a secondary scrolling image.
Nice to have
• High end imagery that speaks to what is being said in the site.
This is not the main image I want to see but I like imagery like this for the main home page.
https://www.pixelmarrow.com/image-photo/couple-hiking-help-each-other-silhouette-731864205
Should not have
• Please do not use dated images or blocky feeling. Please also do not go overboard using the icon in the design.

```html
<!DOCTYPE html>
<html lang="en">
<head>
<meta charset="utf-8">
<title>Summitline Partners</title>
<link rel="stylesheet" href="https://fonts.googleapis.com/css2?family=Michroma&family=Poppins:wght@400;500;600&display=swap">
<style>
:root{
  --blue:#2a87d0;
  --navy:#1d4359;
  --ink:#111418;
  --text:#2f3338;
  --muted:#6b7075;
  --card-grey:#ececec;
  --page:#ffffff;
  --soft:#f6f7f9;
  --line:#c9ccd0;
}
*{box-sizing:border-box;margin:0;padding:0}
html,body{width:1200px;height:3832px;overflow:hidden}
body{position:relative;background:var(--page);font-family:"Poppins",sans-serif;color:var(--text)}
.abs{position:absolute}
.heading{font-family:"Michroma",sans-serif;color:var(--ink);letter-spacing:1px}
.centered{left:0;width:1200px;text-align:center}

/* header */
.brand{left:147px;top:30px;width:170px;text-align:center}
.brand-mark{display:inline-block;width:22px;height:22px;background:var(--blue);margin-bottom:6px}
.brand-name{font-family:"Poppins",sans-serif;font-weight:500;font-size:15px;color:var(--navy);letter-spacing:.5px;line-height:1.2}
.nav{top:43px;font-size:10.5px;color:var(--ink)}
.nav.active{color:var(--blue);font-weight:500}
.btn{display:flex;align-items:center;justify-content:center;background:var(--blue);color:#fff;font-size:11.5px}
.nav-btn{left:952px;top:33px;width:94px;height:35px;font-size:10.5px;box-shadow:0 3px 6px rgba(0,0,0,.15)}

/* hero */
.hero-title{top:270px;font-size:42px;color:#fff;letter-spacing:1px}
.hero-sub{top:334px;font-size:13px;color:#e8edf3;letter-spacing:9px}
.hero-btn{left:540px;top:378px;width:120px;height:40px;font-size:11.5px}
.arrow{top:330px;width:35px;height:35px;background:rgba(255,255,255,.35);display:flex;align-items:center;justify-content:center}

/* sections */
.section-title{font-size:32px}
.divider{left:533px;width:134px;height:12px}
.divider::before,.divider::after{content:"";position:absolute;top:5px;width:48px;height:1px;background:var(--ink)}
.divider::before{left:0}.divider::after{right:0}
.divider span{position:absolute;left:59px;top:0;width:12px;height:12px;background:var(--navy)}
.lead{font-size:11.5px;line-height:30px;color:var(--text)}

.card{background:#fff;box-shadow:0 4px 14px rgba(0,0,0,.1);text-align:center}
.card .icon{width:70px;height:70px;border-radius:50%;background:#fff;box-shadow:0 4px 12px rgba(0,0,0,.12);margin:22px auto 0;display:flex;align-items:center;justify-content:center}
.card h3{font-size:20px;font-weight:600;color:var(--ink);margin-top:30px}
.card p{font-size:11.5px;line-height:22px;margin:18px 16px 0}
.card.featured{background:var(--blue)}
.card.featured h3,.card.featured p{color:#fff}

.outline-btn{left:528px;top:1329px;width:143px;height:51px;border:1px solid var(--ink);display:flex;align-items:center;justify-content:center;font-size:11.5px;color:var(--ink)}

.panel-title{font-size:26px;color:#fff}
.panel-text{font-size:12px;line-height:28.2px;color:#fff}
.panel-btn{width:123px;height:52px}

.quote{font-size:10px;line-height:23.5px;text-align:center;color:var(--text);padding:26px 24px}
.quote.grey{background:var(--card-grey);border-radius:12px}
.quote.blue{background:var(--blue);color:#fff;border-radius:12px}
.avatar{width:64px;height:64px;border-radius:50%;background:linear-gradient(160deg,#cfd6de,#8d99a6)}
.member{font-size:13px;font-weight:600;color:var(--text);text-align:center;width:120px}

/* footer */
.foot-title{font-size:18px;font-weight:600;color:var(--ink)}
.foot-small{font-size:10px;line-height:20px;color:var(--text)}
.field{left:151px;top:3620px;width:273px;height:46px;border:1px solid var(--line);background:#fff}
.links{left:526px;top:3576px;list-style:none;font-size:10px;color:var(--text)}
.links li{display:flex;align-items:center;height:24px}
.links svg{margin-right:12px}
.contact{font-size:10.5px;color:var(--text);display:flex;align-items:center}
.contact svg{margin-right:10px}
.rule{left:141px;top:3771px;width:917px;height:1px;background:#9aa0a6}
.copy{left:153px;top:3793px;font-size:11px;color:var(--text)}
.social{top:3795px;width:16px;height:16px;border-radius:50%;background:#8a9096}
</style>
</head>
<body>

<!-- Header -->
<div class="abs brand">
  <span class="brand-mark"></span>
  <div class="brand-name">SUMMITLINE PARTNERS</div>
</div>
<nav>
  <span class="abs nav active" style="left:604px">Home</span>
  <span class="abs nav" style="left:680px">About Us</span>
  <span class="abs nav" style="left:770px">Our Services</span>
  <span class="abs nav" style="left:879px">Our Team</span>
  <span class="abs btn nav-btn">Work With Us</span>
</nav>

<!-- Hero -->
<svg class="abs" style="left:0;top:97px" width="1200" height="575" viewBox="0 97 1200 575">
  <defs>
    <linearGradient id="heroFill" x1="0" y1="0" x2="0" y2="1">
      <stop offset="0" stop-color="#4a5f80"/>
      <stop offset=".5" stop-color="#8495b0"/>
      <stop offset="1" stop-color="#2f4260"/>
    </linearGradient>
  </defs>
  <path role="img" aria-label="Upward view of glass office towers against a cloudy sky" fill="url(#heroFill)" d="M0,97 H1200 V555 C950,620 600,660 320,648 C180,642 80,622 0,600 Z"/>
  <path fill="none" stroke="var(--blue)" stroke-width="5" d="M0,606 C80,628 180,648 320,654 C600,666 950,626 1200,561"/>
</svg>
<div class="abs centered heading hero-title">SUMMITLINE</div>
<div class="abs centered hero-sub">Curabitur egestas iaculis mi</div>
<div class="abs btn hero-btn">Work With Us</div>
<div class="abs arrow" style="left:52px"><svg width="12" height="14"><path d="M9 1 L3 7 L9 13" fill="none" stroke="#fff" stroke-width="2"/></svg></div>
<div class="abs arrow" style="left:1118px"><svg width="12" height="14"><path d="M3 1 L9 7 L3 13" fill="none" stroke="#fff" stroke-width="2"/></svg></div>

<!-- Services -->
<div class="abs centered heading section-title" style="top:738px">OUR SERVICES</div>
<div class="abs divider" style="top:806px"><span></span></div>
<div class="abs centered lead" style="top:861px">Nulla fermentum leo a nisl sollicitudin fringilla. Cras id auctor augue. Etiam vitae lacus justo. Etiam ut sagittis lacus. Nullam<br>libero lacus, malesuada quis justo malesuada, laoreet placerat justo.</div>

<div class="abs card" style="left:141px;top:968px;width:290px;height:272px">
  <div class="icon"><svg width="34" height="34"><rect x="2" y="2" width="30" height="30" fill="none" stroke="var(--blue)" stroke-width="2"/><rect x="9" y="19" width="4" height="9" fill="var(--blue)"/><rect x="15" y="14" width="4" height="14" fill="var(--blue)"/><rect x="21" y="9" width="4" height="19" fill="var(--blue)"/></svg></div>
  <h3>Marketing</h3>
  <p>In vestibulum ante rhoncus, dignissim nibh sit amet, porta tortor. Proin aliquet orci tellus, vitae euismod</p>
</div>
<div class="abs card featured" style="left:455px;top:1008px;width:289px;height:272px">
  <div class="icon"><svg width="34" height="34"><rect x="6" y="2" width="22" height="30" rx="2" fill="none" stroke="var(--blue)" stroke-width="2"/><circle cx="19" cy="12" r="4" fill="none" stroke="var(--blue)" stroke-width="2"/><path d="M12 21 H24 M12 26 H24" stroke="var(--blue)" stroke-width="2"/></svg></div>
  <h3>Portfolio</h3>
  <p>In vestibulum ante rhoncus, dignissim nibh sit amet, porta tortor. Proin aliquet orci tellus, vitae euismod</p>
</div>
<div class="abs card" style="left:767px;top:968px;width:290px;height:272px">
  <div class="icon"><svg width="38" height="32"><path d="M2 6 H14 L17 9 H36 V30 H2 Z" fill="none" stroke="var(--blue)" stroke-width="2"/><path d="M10 14 V24" stroke="var(--blue)" stroke-width="2"/></svg></div>
  <h3>Construct</h3>
  <p>In vestibulum ante rhoncus, dignissim nibh sit amet, porta tortor. Proin aliquet orci tellus, vitae euismod</p>
</div>
<div class="abs outline-btn">Read More</div>

<!-- About -->
<svg class="abs" style="left:0;top:1420px" width="1200" height="680" viewBox="0 1420 1200 680">
  <defs>
    <clipPath id="aboutClip"><path d="M0,1525 C120,1452 250,1436 400,1440 C700,1450 1000,1500 1200,1530 V2022 C1050,2080 700,2085 500,2075 C300,2065 100,2012 0,1992 Z"/></clipPath>
    <linearGradient id="aboutPhoto" x1="0" y1="0" x2="1" y2="1">
      <stop offset="0" stop-color="#5c7a48"/>
      <stop offset=".45" stop-color="#c9b6ad"/>
      <stop offset="1" stop-color="#e6e8ea"/>
    </linearGradient>
  </defs>
  <g clip-path="url(#aboutClip)">
    <rect role="img" aria-label="Businesswoman on a phone call working at a laptop" x="0" y="1420" width="588" height="680" fill="url(#aboutPhoto)"/>
    <rect x="588" y="1420" width="612" height="680" fill="var(--navy)"/>
  </g>
  <path fill="none" stroke="var(--blue)" stroke-width="5" d="M0,1521 C120,1448 250,1432 400,1436 C700,1446 1000,1496 1200,1526"/>
  <path fill="none" stroke="var(--blue)" stroke-width="5" d="M0,1998 C100,2018 300,2071 500,2081 C700,2091 1050,2086 1200,2028"/>
</svg>
<div class="abs heading panel-title" style="left:684px;top:1585px">ABOUT US</div>
<div class="abs panel-text" style="left:684px;top:1648px;width:440px">Nulla sit amet arcu elit. Nulla ultricies metus sed lacus feugiat cursus. Suspendisse potenti. Duis ligula quam, dignissim ut ornare quis, ultricies vel felis. Praesent venenatis dignissim ligula. Fusce sit amet mi augue. Nullam aliquet metus diam, ac auctor nulla dictum at. Nunc mi nisi, bibendum ut aliquet quis, imperdiet non enim. Etiam convallis egestas tincidunt. Etiam lacinia, augue vel convallis euismod, metus lacus posuere purus, sit amet auctor enim nisl vitae felis. Donec vulputate ut nisi vitae ullamcorper. Class aptent taciti sociosqu ad litora torquent per conubia nostra, per inceptos</div>
<div class="abs btn panel-btn" style="left:683px;top:1928px">Read More</div>

<!-- Team -->
<div class="abs" style="left:0;top:2110px;width:1200px;height:720px;background:var(--soft)"></div>
<div class="abs centered heading section-title" style="top:2191px">OUR TEAM</div>
<div class="abs divider" style="top:2256px"><span></span></div>
<div class="abs centered lead" style="top:2293px">Mauris quis tempus nibh, sagittis ornare ligula. Vivamus pharetra, arcu quis malesuada mollis, enim risus<br>suscipit libero, vitae lacinia libero massa id diam.</div>

<div class="abs quote grey" style="left:141px;top:2418px;width:259px;height:199px">Nemo enim ipsam voluptatem quia voluptas sit aspernatur aut odit aut fugit, sed quia consequuntur magni dolores eos qui ratione voluptatem sequi nesciunt. Neque porro quisquam est, qui dolorem ipsum quia dolor sit amet, consectetur,</div>
<div class="abs quote blue" style="left:447px;top:2402px;width:301px;height:230px;font-size:10.5px;line-height:25px;padding-top:30px">Nemo enim ipsam voluptatem quia voluptas sit aspernatur aut odit aut fugit, sed quia consequuntur magni dolores eos qui ratione voluptatem sequi nesciunt. Neque porro quisquam est, qui dolorem ipsum quia dolor sit amet, consectetur, adipisci velit,</div>
<svg class="abs" style="left:586px;top:2631px" width="22" height="12"><path d="M0 0 H22 L11 11 Z" fill="var(--blue)"/></svg>
<div class="abs quote grey" style="left:800px;top:2418px;width:260px;height:199px">Nemo enim ipsam voluptatem quia voluptas sit aspernatur aut odit aut fugit, sed quia consequuntur magni dolores eos qui ratione voluptatem sequi nesciunt. Neque porro quisquam est, qui dolorem ipsum quia dolor sit amet, consectetur, adipisci velit,</div>

<div class="abs avatar" role="img" aria-label="Portrait of Joy" style="left:238px;top:2640px"></div>
<div class="abs member" style="left:210px;top:2718px">JOY</div>
<div class="abs avatar" role="img" aria-label="Portrait of Dan" style="left:566px;top:2668px"></div>
<div class="abs member" style="left:538px;top:2747px">DAN</div>
<div class="abs avatar" role="img" aria-label="Portrait of Omera" style="left:898px;top:2637px"></div>
<div class="abs member" style="left:870px;top:2715px">OMERA</div>

<!-- Work with us -->
<svg class="abs" style="left:0;top:2810px" width="1200" height="680" viewBox="0 2810 1200 680">
  <defs>
    <clipPath id="workClip"><path d="M0,2905 C300,2862 700,2832 900,2826 C1050,2822 1150,2830 1200,2840 V3375 C1000,3440 700,3475 450,3470 C250,3466 100,3446 0,3430 Z"/></clipPath>
    <linearGradient id="workPhoto" x1="0" y1="0" x2="1" y2="1">
      <stop offset="0" stop-color="#8a8d90"/>
      <stop offset=".5" stop-color="#d5d7d9"/>
      <stop offset="1" stop-color="#5c6063"/>
    </linearGradient>
  </defs>
  <g clip-path="url(#workClip)">
    <rect x="0" y="2810" width="614" height="680" fill="var(--navy)"/>
    <rect role="img" aria-label="Black and white view up between tall office buildings" x="614" y="2810" width="586" height="680" fill="url(#workPhoto)"/>
  </g>
  <path fill="none" stroke="var(--blue)" stroke-width="5" d="M0,2899 C300,2856 700,2826 900,2820 C1050,2816 1150,2824 1200,2834"/>
  <path fill="none" stroke="var(--blue)" stroke-width="5" d="M0,3436 C100,3452 250,3472 450,3476 C700,3481 1000,3446 1200,3381"/>
</svg>
<div class="abs heading panel-title" style="left:88px;top:2988px">WORK WITH US</div>
<div class="abs panel-text" style="left:88px;top:3049px;width:440px">Interdum et malesuada fames ac ante ipsum primis in faucibus. Morbi non posuere augue. Cras vehicula erat non lorem placerat vestibulum. Aenean suscipit varius tellus. Quisque mattis ut purus sed ultrices. Morbi condimentum dui felis. Nullam facilisis justo eget imperdiet interdum. Aenean tempus porta diam, id vehicula augue tristique vel. Morbi sodales odio purus, quis viverra ligula mattis quis. Curabitur dictum rutrum nibh, eu pharetra massa luctus sit amet. Vestibulum nunc leo, venenatis eget ante in, mollis accumsan lorem. Maecenas urna turpis, consectetur ut hendrerit quis, malesuada in sapien.</div>
<div class="abs btn panel-btn" style="left:87px;top:3330px">Contact Foam</div>

<!-- Footer -->
<div class="abs foot-title" style="left:153px;top:3518px">Stay Connected</div>
<div class="abs foot-small" style="left:153px;top:3558px;width:280px">Curabitur egestas iaculis mi, non volutpat ipsum eleifend at</div>
<div class="abs field"></div>
<div class="abs btn" style="left:151px;top:3680px;width:273px;height:45px;font-size:14px">Sign Up</div>

<div class="abs foot-title" style="left:518px;top:3526px">Site Links</div>
<ul class="abs links">
  <li><svg width="12" height="12"><circle cx="6" cy="6" r="5" fill="none" stroke="var(--blue)"/><path d="M3.5 6 L5.5 8 L8.5 4" fill="none" stroke="var(--blue)"/></svg>Home</li>
  <li><svg width="12" height="12"><circle cx="6" cy="6" r="5" fill="none" stroke="var(--blue)"/><path d="M3.5 6 L5.5 8 L8.5 4" fill="none" stroke="var(--blue)"/></svg>About Us</li>
  <li><svg width="12" height="12"><circle cx="6" cy="6" r="5" fill="none" stroke="var(--blue)"/><path d="M3.5 6 L5.5 8 L8.5 4" fill="none" stroke="var(--blue)"/></svg>Our Services</li>
  <li><svg width="12" height="12"><circle cx="6" cy="6" r="5" fill="none" stroke="var(--blue)"/><path d="M3.5 6 L5.5 8 L8.5 4" fill="none" stroke="var(--blue)"/></svg>Our Team</li>
  <li><svg width="12" height="12"><circle cx="6" cy="6" r="5" fill="none" stroke="var(--blue)"/><path d="M3.5 6 L5.5 8 L8.5 4" fill="none" stroke="var(--blue)"/></svg>Work With Us</li>
</ul>

<div class="abs" style="left:724px;top:3530px;width:260px;text-align:center">
  <span class="brand-mark" style="width:30px;height:30px;margin-bottom:10px"></span>
  <div class="brand-name" style="font-size:19px">SUMMITLINE PARTNERS</div>
</div>
<div class="abs contact" style="left:726px;top:3650px"><svg width="14" height="14"><path d="M2 2 C2 8 6 12 12 12 L12 9 L9 8 L8 9.5 C6 8.5 5.5 8 4.5 6 L6 5 L5 2 Z" fill="var(--blue)"/></svg>555-014-2290</div>
<div class="abs contact" style="left:846px;top:3650px"><svg width="14" height="11"><rect x="0.5" y="0.5" width="13" height="10" fill="var(--blue)"/><path d="M0.5 0.5 L7 6 L13.5 0.5" fill="none" stroke="#fff"/></svg>hello@summitline.example</div>
<div class="abs contact" style="left:724px;top:3688px"><svg width="12" height="16"><path d="M6 15 C2 10 1 8 1 6 A5 5 0 0 1 11 6 C11 8 10 10 6 15 Z" fill="var(--blue)"/><circle cx="6" cy="6" r="2" fill="#fff"/></svg>48 Alder Court, Ridgefield, MN 55190</div>

<div class="abs rule"></div>
<div class="abs copy">© 2020 Summitline Partners | Privacy Policy · Terms of Use</div>
<span class="abs social" role="img" aria-label="Social link" style="left:952px"></span>
<span class="abs social" role="img" aria-label="Social link" style="left:982px"></span>

</body>
</html>
```